Business Card design for a mobile solutions company

- we are a mobile telecommunications company focusing on mobile content and solutions
- we are based in Malaysia however operate a regional business
- attached is our company logo and current business card design
- please try to incorporate the "cubes" into the design

our company philosophy is dynamic and outgoing. we are a lean team of less than 50, but we have strong roots in the mobile industry in Asia and we like to challenge ourselves by taking on larger projects.

we love joint ventures and working with partners to find the right solutions for our clients

*please feel free to modify our logo (typeface etc)
**we would like to keep the 3 cube design for the logo, but I would love to see different versions of it

some of the designs are great and I think our logo (especially the typeface used for the words) doesn't look good. please feel free to update the logo but try to keep the cubes, you are free to modify the cubes and update them.

Reason: looking for more design please

Industry/Entity Type

Telecommunications

Font styles to use
Sans Serif

```html
<!DOCTYPE html>
<html lang="en">
<head>
<meta charset="utf-8">
<title>Nova Reach – Business Card</title>
<link rel="stylesheet" href="https://fonts.googleapis.com/css2?family=Arimo:wght@400;700&family=Roboto+Slab:wght@300;800&display=swap">
<style>
  :root {
    --page: #e6e3df;
    --card-red: #e41b23;
    --panel-dark: #1c1c1e;
    --panel-deep: #0d0d0e;
    --ring: #e41b23;
    --ink-light: #ffffff;
    --ink-muted: #c9c9c9;
  }
  * { margin: 0; padding: 0; box-sizing: border-box; }
  html, body { width: 1200px; height: 900px; overflow: hidden; }
  body { background: var(--page); font-family: "Arimo", Arial, sans-serif; }
  .canvas { position: relative; width: 1200px; height: 900px; }

  .card {
    position: absolute; left: 260px; width: 680px; height: 390px;
    box-shadow: 0 10px 24px rgba(0,0,0,.25);
  }
  .card--front { top: 45px; }
  .card--back { top: 465px; }
  .card svg { position: absolute; inset: 0; }

  .brand-name {
    position: absolute; left: 250px; top: 118px; width: 400px; text-align: center;
    font-weight: 700; font-size: 54px; letter-spacing: 1px; color: var(--ink-light);
  }
  .person-name {
    position: absolute; left: 250px; top: 186px; width: 400px; text-align: center;
    font-family: "Roboto Slab", Georgia, serif; font-weight: 300;
    font-size: 28px; letter-spacing: 3px; color: var(--ink-muted);
  }
  .person-title {
    position: absolute; left: 250px; top: 224px; width: 400px; text-align: center;
    font-family: "Roboto Slab", Georgia, serif; font-weight: 300;
    font-size: 15px; color: var(--ink-muted);
  }

  .contact-line {
    position: absolute; left: 128px; font-size: 21px; color: var(--ink-light);
  }
  .address {
    position: absolute; font-size: 15px; line-height: 1.35; color: var(--ink-light);
  }
  .address--office { left: 128px; top: 262px; font-weight: 700; }
  .address--street { left: 350px; top: 262px; }
</style>
</head>
<body>
<main class="canvas">

  <section class="card card--front" aria-label="Card front">
    <svg width="680" height="390" viewBox="0 0 680 390">
      <defs>
        <linearGradient id="panelShade" x1="0" y1="0" x2="1" y2="1">
          <stop offset="0" stop-color="#2a2a2c"/>
          <stop offset="1" stop-color="#0d0d0e"/>
        </linearGradient>
      </defs>
      <rect class="card-base" width="680" height="390" fill="var(--card-red)"/>
      <path class="dark-panel" role="img" aria-label="Dark quilted diamond texture"
            d="M200 22 H660 V368 H200 A200 200 0 0 1 200 22 Z" fill="url(#panelShade)"/>
      <circle class="emblem-disc" cx="112" cy="250" r="74" fill="var(--panel-deep)" stroke="var(--ring)" stroke-width="8"/>
    </svg>
    <div class="brand-name">NOVA REACH</div>
    <div class="person-name">LENA MARSH</div>
    <div class="person-title">Chief Marketing Officer</div>
  </section>

  <section class="card card--back" aria-label="Card back">
    <svg width="680" height="390" viewBox="0 0 680 390">
      <defs>
        <linearGradient id="panelShadeBack" x1="0" y1="0" x2="1" y2="1">
          <stop offset="0" stop-color="#2a2a2c"/>
          <stop offset="1" stop-color="#0d0d0e"/>
        </linearGradient>
      </defs>
      <rect class="card-base" width="680" height="390" fill="var(--card-red)"/>
      <path class="dark-panel" role="img" aria-label="Dark quilted diamond texture"
            d="M20 22 H480 A200 200 0 0 1 480 368 H20 Z" fill="url(#panelShadeBack)"/>
      <circle class="emblem-disc" cx="592" cy="82" r="62" fill="var(--panel-deep)" stroke="var(--ring)" stroke-width="8"/>

      <g class="contact-tab">
        <rect x="20" y="88" width="88" height="34" fill="var(--card-red)"/>
        <path d="M80 95 q-6 0 -8 4 q4 10 12 16 q4 -2 4 -8 l-5 -3 -2 3 q-4 -3 -6 -7 l3 -2 z" fill="var(--ink-light)"/>
      </g>
      <g class="contact-tab">
        <rect x="20" y="138" width="88" height="34" fill="var(--card-red)"/>
        <rect x="74" y="143" width="14" height="24" rx="2" fill="none" stroke="var(--ink-light)" stroke-width="2.5"/>
        <rect x="77" y="147" width="8" height="10" fill="var(--ink-light)"/>
      </g>
      <g class="contact-tab">
        <rect x="20" y="188" width="88" height="34" fill="var(--card-red)"/>
        <rect x="70" y="196" width="22" height="16" fill="none" stroke="var(--ink-light)" stroke-width="2.5"/>
        <path d="M70 196 l11 9 11 -9" fill="none" stroke="var(--ink-light)" stroke-width="2.5"/>
      </g>
    </svg>
    <div class="contact-line" style="top:56px">60 3 555 0142</div>
    <div class="contact-line" style="top:104px">62 855 5550199</div>
    <div class="contact-line" style="top:152px">lena@novareach.com.my</div>
    <div class="address address--office">Nova Reach SDN BHD<br>Unit 5-1, Level 5, Block 2<br>The Meridian</div>
    <div class="address address--street">Lorong Cerah No.12<br>Jalan Damai<br>50450 Kuala Lumpur</div>
  </section>

</main>
</body>
</html>
```